Zielgruppe
wir sind ein ambulanter Pflegedienst
Aufgabenstellung
Es soll ein Flyer entworfen werden.
Im Vordergrund steht die Behandlungspflege. Patienten sollen darauf aufmerksam gemacht werden, dass wir Insulininjektionen übernehmen und Kompressionsstrümpfe anziehen, wenn der Hausarzt dafür eine Verordnung ausstellt.
Im Vordergrund steht die Insulininjektion und das an und ausziehen der Kompressionsstrümpfe.
Falls die Patienten es nicht mehr alleine schaffen, springt der Pflegedienst ein.
Wichtig ist, dass das Pflegegeld nicht gekürzt wird, da dies eine Leistung der Krankenkasse ist.
Daten des Pflegedienstes:
Pflegehaus Lindental
Birkenweg 27
18057 Rostock
Tel 0800 4417236
www.Pflegehaus-Lindental.de
info@Pflegehaus-Lindental.de

```html
<!DOCTYPE html>
<html lang="de">
<head>
<meta charset="utf-8">
<title>Pflegehaus Lindental – Flyer</title>
<link rel="stylesheet" href="https://fonts.googleapis.com/css2?family=Open+Sans:ital,wght@0,400;0,700;0,800;1,300;1,700&family=Rubik:wght@800&display=swap">
<style>
  :root {
    --blue: #0050e6;
    --orange: #ff7f2a;
    --green: #76ff33;
    --white: #ffffff;
    --ink: #111111;
  }
  * { margin: 0; padding: 0; box-sizing: border-box; }
  html, body { width: 846px; height: 1200px; overflow: hidden; background: var(--white); }
  .flyer {
    position: relative; width: 846px; height: 1200px; overflow: hidden;
    font-family: "Open Sans", sans-serif;
  }
  .photo-area {
    position: absolute; inset: 0;
    background:
      radial-gradient(ellipse 260px 330px at 130px 230px, #c98f6e 0%, rgba(201,143,110,0) 100%),
      radial-gradient(ellipse 260px 300px at 720px 400px, #c8815c 0%, rgba(200,129,92,0) 100%),
      radial-gradient(ellipse 300px 260px at 90px 950px, #8a4a36 0%, rgba(138,74,54,0) 100%),
      radial-gradient(ellipse 320px 260px at 650px 900px, #b8c7d9 0%, rgba(184,199,217,0) 100%),
      linear-gradient(180deg, #cbc3b6 0%, #e9e6e3 35%, #eef0f3 70%, #dfe3e8 100%);
  }
  .frame { position: absolute; inset: 0; pointer-events: none; }

  .headline {
    position: absolute; left: 21px; color: var(--white);
    background: var(--orange); font-family: "Rubik", sans-serif; font-weight: 800;
    white-space: nowrap; text-transform: uppercase;
  }
  .headline--main {
    top: 40px; width: 784px; height: 70px; padding-left: 5px;
    font-size: 60px; line-height: 72px; letter-spacing: -1px;
    clip-path: polygon(0 0, 100% 0, 98% 100%, 0 100%);
  }
  .headline--sub {
    top: 121px; width: 808px; height: 51px; padding-left: 5px;
    font-size: 36px; line-height: 52px; letter-spacing: -1px;
    clip-path: polygon(0 0, 100% 0, 98.4% 100%, 0 100%);
  }

  .brand {
    position: absolute; left: 70px; top: 252px; width: 400px; text-align: center;
  }
  .brand__ring {
    display: block; margin: 0 auto;
  }
  .brand__name {
    margin-top: 18px; font-size: 40px; font-weight: 700; color: var(--blue); line-height: 1.1;
  }

  .contact { position: absolute; left: 449px; top: 289px; list-style: none; }
  .contact li {
    display: block; width: fit-content; min-width: 260px; height: 32px; margin-bottom: 3px;
    padding: 0 4px; background: var(--green); color: var(--ink);
    font-size: 25px; line-height: 32px; white-space: nowrap;
  }

  .services { position: absolute; left: 41px; top: 753px; }
  .services span {
    display: block; width: fit-content; height: 44px; margin-bottom: 4px;
    padding: 0 22px 0 6px; background: var(--blue); color: var(--white);
    font-style: italic; font-weight: 700; font-size: 35px; line-height: 44px;
    letter-spacing: -0.5px; white-space: nowrap;
    clip-path: polygon(0 0, 100% 0, calc(100% - 8px) 100%, 0 100%);
  }

  .hotline-band { position: absolute; left: 0; top: 1075px; }
  .hotline {
    position: absolute; left: 20px; top: 1130px; display: flex; align-items: center;
    color: var(--white); white-space: nowrap;
  }
  .hotline__number { margin-left: 18px; font-weight: 800; font-size: 72px; line-height: 1; letter-spacing: -1px; }
  .hotline__note { margin-left: 8px; font-style: italic; font-weight: 300; font-size: 42px; }
</style>
</head>
<body>
<main class="flyer">
  <div class="photo-area" role="img" aria-label="Unscharfes Foto: Pflegekraft im hellen Kittel betreut lächelnd einen älteren Patienten"></div>

  <svg class="frame" width="846" height="1200" aria-hidden="true">
    <rect x="6" y="3" width="834" height="1194" fill="none" stroke="#0050e6" stroke-width="5" stroke-dasharray="14 9"/>
  </svg>

  <h1 class="headline headline--main">Wir kümmern uns um Sie !</h1>
  <h2 class="headline headline--sub">Ohne dass Ihr Pflegegeld gekürzt wird !</h2>

  <div class="brand">
    <svg class="brand__ring" width="270" height="270" viewBox="0 0 270 270" aria-hidden="true">
      <circle cx="135" cy="135" r="126" fill="none" stroke="#0050e6" stroke-width="16"/>
    </svg>
    <p class="brand__name">Pflegehaus Lindental</p>
  </div>

  <ul class="contact">
    <li>Pflegehaus Lindental</li>
    <li>Birkenweg 27</li>
    <li>18057 Rostock</li>
    <li>Tel.: 0800 4417236</li>
    <li>www.Pflegehaus-Lindental.de</li>
    <li>info@Pflegehaus-Lindental.de</li>
  </ul>

  <p class="services">
    <span>Sowohl bei Insulininjektionen,als auch beim</span>
    <span>anziehen von Kompressionsstrümpfen sind</span>
    <span>wir jederzeit für Sie da !</span>
  </p>

  <svg class="hotline-band" width="846" height="125" aria-hidden="true">
    <path d="M0 2 Q423 80 846 2 L846 125 L0 125 Z" fill="#0050e6"/>
  </svg>
  <div class="hotline">
    <svg width="50" height="50" viewBox="0 0 50 50" aria-hidden="true">
      <circle cx="25" cy="25" r="22" fill="none" stroke="#fff" stroke-width="4"/>
      <path d="M16 13 l6 -2 l3 8 l-4 3 q3 6 8 9 l3 -4 l8 3 l-2 6 q-12 1 -19 -8 q-6 -7 -3 -15 z" fill="#fff"/>
    </svg>
    <span class="hotline__number">0800 44172 36</span>
    <span class="hotline__note">(kostenlos)</span>
  </div>
</main>
</body>
</html>
```